TOR Capital Allies LLC a High Risk Big Rewards company for Rich Young Entrepreneurs

We would like a very modern, powerful in the eyes of our customers, modern, minimalist feel, financial gain. this business card is for young Rich entrepreneurs who want to invest money into High Risk, Big Rewards Businesses. The card Should sell the business!! let your creativity go Wild! I pick most of the designers for this project because of your BOLD Designs, I would like this card to be Bold, Modern, Minimalist, use as many effects in your graphic Artist Mind, Do not let the Financial sound of this business to make you think Conservative that's the last thing we are! if you have a lot of money and you want to play a risky market call US
Updates

Project Deadline Extended
Reason: have not received, enough designs to choose 1st and second place, sure I have received over 100 designs but it seems most designers are submitting every card they have ever made before and calling it mine, please we are looking for fresh ideas please!

Target Market(s)

Private Risky Investors

Industry/Entity Type

Financial

Contact Information for Business Card

powerful in the eyes of our customers,modern, minimalist feel

Font styles to use
Other font styles liked:
• Modern feeling fonts

Requirements
Must have
• The Company Name is TOR Capital Allies LLC and it must be on the CARD
• My Name, title, Cell , email
• Dalton Fairweather G.E.D.
• Managing Member
• 404.658.1937
• dalton@torcapitalallies.example
Nice to have
• try a black thick plastic card with round corners with Dalton Fairweather GED (make sure GED is smaller than name) just on one side of the card, and my phone number with out the icons and email on the other side, this card should look like a exclusive credit card or exclusive VIP card, something you would never loose

```html
<!DOCTYPE html>
<html lang="en">
<head>
<meta charset="utf-8">
<title>TOR Capital Allies LLC — Business Card</title>
<link rel="stylesheet" href="https://fonts.googleapis.com/css2?family=Della+Respira&display=swap">
<style>
  :root {
    --card-black: #000000;
    --ink-white: #ffffff;
    --glow-red: #ff2a55;
    --glow-deep: #c4002e;
  }
  html, body {
    margin: 0;
    padding: 0;
    width: 1200px;
    height: 686px;
    overflow: hidden;
    background: var(--card-black);
  }
  .card {
    position: relative;
    width: 1200px;
    height: 686px;
    background: var(--card-black);
    font-family: "Della Respira", Georgia, serif;
    color: var(--ink-white);
  }
  .company-name {
    position: absolute;
    left: 63px;
    top: 118px;
    margin: 0;
    font-family: "Della Respira", Georgia, serif;
    font-weight: 400;
    font-size: 50px;
    line-height: 60px;
    white-space: nowrap;
    color: var(--ink-white);
  }
  .contact {
    position: absolute;
    inset: 0;
  }
  .contact p {
    position: absolute;
    right: 72px;
    margin: 0;
    line-height: 1;
    white-space: nowrap;
    color: var(--ink-white);
    text-shadow:
      0 0 3px var(--glow-red),
      0 0 6px var(--glow-red),
      0 0 12px var(--glow-deep),
      0 0 18px var(--glow-deep);
  }
  .person-name  { top: 312px; font-size: 45px; }
  .person-title { top: 396px; font-size: 45px; }
  .person-phone { top: 480px; font-size: 45px; letter-spacing: 1px; }
  .contact .person-email { top: 565px; right: 86px; font-size: 43px; }
</style>
</head>
<body>
  <main class="card">
    <h1 class="company-name">TOR Capital Allies LLC</h1>
    <section class="contact">
      <p class="person-name">Dalton Fairweather G.E.D.</p>
      <p class="person-title">Managing Member</p>
      <p class="person-phone">404.658.1937</p>
      <p class="person-email">dalton@torcapitalallies.example</p>
    </section>
  </main>
</body>
</html>
```